Sell the dream! Property investment proposal document

We are looking for a proposal document which outlines our vision for property development. The purpose of the document is to raise investment from investors - sell the dream!
Brief summary:
Tarrow Dwellings Developments, is an emerging New Zealand property investment company with a focus on providing unique property investment opportunities.
Our expertise and capabilities in architectural modular homes provide us with a remarkable advantage in tackling the development of properties that are typically considered challenging, remote, or uniquely positioned.
Our specialization in this niche sector of property development not only sets us apart from competitors, but also paves the way for lucrative investment opportunities in the New Zealand property market.
Feel free to use any images from www.tarrowdwellings.co.nz
Target Market(s)
investors for a unique property development opportunity
Industry/Entity Type
luxury property development in unique locations throughout New Zealand
Font styles to use
Colors
Designer to choose only greyscale colors for use in the design.
Look and feel

```html
<!DOCTYPE html>
<html lang="en">
<head>
<meta charset="utf-8">
<title>Tarrow Dwellings Developments – Investment Proposal</title>
<link href="https://fonts.googleapis.com/css2?family=Josefin+Sans:wght@300;400;600;700&family=Poppins:ital,wght@0,300;0,400;0,600;1,300&display=swap" rel="stylesheet">
<style>
  :root{
    --page-bg:#e4e5e6;
    --sheet:#2b2b2b;
    --pattern-tone:#313131;
    --frame:#8c8c8c;
    --text:#e6e6e6;
    --muted:#9b9b9b;
    --heading-light:#d2d2d2;
    --heading-bold:#a2a2a2;
    --bar:#cfcfcf;
    --bar-text:#2b2b2b;
  }
  *{box-sizing:border-box;margin:0;padding:0}
  html,body{width:1200px;height:2975px;overflow:hidden;background:var(--page-bg)}
  body{position:relative;font-family:"Poppins",sans-serif;color:var(--text)}
  .spread{position:absolute;left:193px;width:814px;height:575px;background:var(--sheet);overflow:hidden}
  .spread--cover{top:912px}
  .spread--overview{top:1553px}
  .spread--advantage{top:2205px}
  .pattern-zone{position:absolute;background:var(--pattern-tone)}
  .photo{position:absolute;border:1px solid #bdbdbd}
  .frame{position:absolute;border:1px solid var(--frame)}
  .wordmark{position:absolute;font-family:"Josefin Sans",sans-serif;font-weight:400;color:#fff;letter-spacing:-1px;line-height:1}
  .contact-list{position:absolute;left:105px;top:450px;list-style:none;font-size:12px}
  .contact-list li{display:flex;align-items:center;height:23px}
  .contact-list svg{width:10px;height:10px;margin-right:10px}
  .follow{position:absolute;left:316px;top:493px;font-size:8px;letter-spacing:2px;text-align:center;line-height:1.3}
  .follow .dots{display:flex;gap:4px;justify-content:center;margin-top:3px}
  .follow .dots span{width:11px;height:11px;border-radius:50%;background:var(--muted)}
  .cover-title{position:absolute;left:434px;top:375px;font-family:"Josefin Sans",sans-serif;font-size:26px;line-height:1.05}
  .cover-title .light{font-weight:300;color:var(--heading-light)}
  .cover-title .bold{font-weight:700;color:var(--heading-bold)}
  .tagline{position:absolute;left:435px;top:440px;font-size:10px;letter-spacing:3px;line-height:1.45}
  .tagline .dim{color:var(--muted)}
  .company-type{position:absolute;left:436px;top:508px;font-size:9px;letter-spacing:3px;color:var(--muted);line-height:1.3}
  .url-bar{position:absolute;left:580px;top:508px;width:234px;height:22px;background:var(--bar);color:var(--bar-text);font-size:11px;letter-spacing:2.5px;display:flex;align-items:center;padding-left:12px}
  .url-bar b{font-weight:600}
  .section-title{position:absolute;font-family:"Josefin Sans",sans-serif;font-size:28px;line-height:1.02}
  .section-title .light{display:block;font-weight:300;color:var(--heading-light)}
  .section-title .bold{display:block;font-weight:700;color:var(--heading-bold)}
  .dot-rule{position:absolute;width:44px;height:2px;background:repeating-linear-gradient(90deg,var(--muted) 0 2px,transparent 2px 5px)}
  .body-copy{position:absolute;font-size:7.4px;line-height:1.35;color:var(--text);font-weight:300}
  .body-copy p{margin-bottom:9px}
  .body-copy .note{font-style:italic}
  .page-footer{position:absolute;top:518px;width:320px;height:12px;display:flex;align-items:center;font-size:7px;letter-spacing:2px;color:var(--muted)}
  .page-footer .rule{flex:1;height:1px;background:#555;margin:0 6px}
  .page-footer .num{width:11px;height:11px;border-radius:50%;background:#888;color:var(--sheet);font-size:6px;letter-spacing:0;display:flex;align-items:center;justify-content:center}
</style>
</head>
<body>

<section class="spread spread--cover">
  <div class="pattern-zone" style="left:0;top:0;width:80px;height:575px" role="img" aria-label="Faint geometric background pattern"></div>
  <div class="pattern-zone" style="left:658px;top:0;width:156px;height:575px" role="img" aria-label="Faint geometric background pattern"></div>

  <div class="frame" style="left:80px;top:30px;width:222px;height:215px"></div>
  <div class="photo" style="left:0;top:46px;width:283px;height:221px;background:linear-gradient(180deg,#b9b3a8 0%,#8f8a80 35%,#4d4f35 65%,#2f3022 100%)" role="img" aria-label="Aerial view of a low dark home on a coastal hillside"></div>
  <div class="frame" style="left:78px;top:198px;width:172px;height:200px"></div>
  <div class="photo" style="left:105px;top:210px;width:239px;height:160px;background:linear-gradient(180deg,#f2f3f3 0%,#d9dcdc 30%,#2d2d2d 48%,#555 62%,#6d8a3a 82%,#4f6a28 100%)" role="img" aria-label="Dark cantilevered modular home over a grassy rock outcrop"></div>

  <div class="wordmark" style="left:105px;top:385px;font-size:36px">Tarrow</div>

  <ul class="contact-list">
    <li><svg viewBox="0 0 10 10"><circle cx="5" cy="5" r="5" fill="#8a8a8a"/><path d="M3 2.5l1 1-.6.8c.4.9 1 1.5 1.9 1.9l.8-.6 1 1-.7.9C4.6 7.3 2.7 5.4 2.2 3.2z" fill="#2b2b2b"/></svg>09 555 0142</li>
    <li><svg viewBox="0 0 10 10"><circle cx="5" cy="5" r="5" fill="#8a8a8a"/><path d="M5 2a2 2 0 0 1 2 2c0 1.5-2 4-2 4S3 5.5 3 4a2 2 0 0 1 2-2z" fill="#2b2b2b"/></svg>Harlow Bay, Auckland</li>
    <li><svg viewBox="0 0 10 10"><circle cx="5" cy="5" r="5" fill="#8a8a8a"/><rect x="2.5" y="3.3" width="5" height="3.4" fill="#2b2b2b"/></svg>sales@tarrowdwellings.co.nz</li>
    <li><svg viewBox="0 0 10 10"><circle cx="5" cy="5" r="5" fill="#8a8a8a"/><circle cx="5" cy="5" r="2.6" fill="none" stroke="#2b2b2b" stroke-width=".8"/></svg>www.tarrowdwellings.co.nz</li>
  </ul>

  <div class="follow">FOLLOW<br>US ON<div class="dots"><span></span><span></span></div></div>

  <div class="wordmark" style="left:435px;top:36px;font-size:54px">Tarrow</div>
  <div class="frame" style="left:475px;top:113px;width:303px;height:200px"></div>
  <div class="photo" style="left:437px;top:128px;width:326px;height:222px;background:linear-gradient(180deg,#5b5a55 0%,#c9b78f 30%,#e6d29f 45%,#8a8a86 60%,#6f6a62 80%,#8a8479 100%)" role="img" aria-label="Glass pavilion home overlooking the sea at sunset"></div>

  <h1 class="cover-title"><span class="light">TARROW DWELLINGS</span><br><span class="bold">DEVELOPMENTS</span></h1>
  <p class="tagline"><span class="dim">AN EMERGING</span><br>NEW ZEALAND PROPERTY</p>
  <p class="company-type">INVESTMENT<br>COMPANY</p>
  <div class="url-bar">www.<b>tarrowdwellings</b>.co.nz</div>
</section>

<section class="spread spread--overview">
  <div class="pattern-zone" style="left:395px;top:0;width:170px;height:575px" role="img" aria-label="Faint geometric background pattern"></div>

  <h2 class="section-title" style="left:46px;top:52px"><span class="light">BUSINESS</span><span class="bold">OVERVIEW</span></h2>
  <div class="frame" style="left:283px;top:96px;width:214px;height:244px"></div>
  <div class="photo" style="left:47px;top:112px;width:494px;height:206px;background:linear-gradient(180deg,#dfe3e6 0%,#b8bec2 25%,#3a3a38 45%,#2a2a28 65%,#56603f 82%,#a6a8a5 100%)" role="img" aria-label="Two-storey dark timber modular home with landscaped garden and driveway"></div>

  <div class="body-copy" style="left:45px;top:352px;width:310px">
    <p>Our expertise and capabilities in architectural modular homes provide us with a remarkable advantage in tackling the development of properties that are typically considered challenging, remote, or uniquely positioned.</p>
    <p>As a company, with 48 employees boasting a wealth of experience in handling complex architectural projects, making us well-equipped to navigate the intricacies and demands of such ventures.</p>
    <p>This advantage allows us to not only execute projects efficiently but also to deliver exceptional results within condensed time frames.</p>
    <p>By capitalizing on our ability to develop difficult, remote, or one-of-a-kind properties swiftly and effectively, Tarrow Dwellings Developments offers investors a rare chance to engage in projects that promise exceptional profitability in the New Zealand property market.</p>
  </div>

  <h2 class="section-title" style="left:568px;top:52px"><span class="light">BUSINESS</span><span class="bold">ORIGIN</span></h2>
  <div class="dot-rule" style="left:570px;top:120px"></div>
  <div class="body-copy" style="left:568px;top:137px;width:182px">
    <p>Tarrow Dwellings Developments was established with the goal of transforming the property investment market in New Zealand by introducing an innovative approach that centers on architectural modular designs and streamlined project timelines.</p>
    <p>Driven by our enthusiasm for architecture and real estate, we have expanded our successful business model to not only offer financial opportunities for investors but also to expand on our passion for high-end architectural design.</p>
    <p>With a wealth of experience accumulated over the past six years in the construction and the property market, we are pivoting to focus solely on our property development initiatives, presenting completed Tarrow projects to the market, in exclusive locations.</p>
    <p>These projects will boast high-quality standards, meticulous attention to detail and landscaping, and creative design elements. By introducing completed Tarrow properties into the market, we aim to reach a wider audience, catering to individuals who prefer ready-to-occupy homes, over engaging in the design and construction process. This approach also simplifies the financing process for prospective buyers, as established properties are often preferred by financial lenders.</p>
  </div>

  <div class="page-footer" style="left:45px">www.tarrowdwellings.co.nz<span class="rule"></span><span class="num">1</span></div>
  <div class="page-footer" style="left:450px">www.tarrowdwellings.co.nz<span class="rule"></span><span class="num">2</span></div>
</section>

<section class="spread spread--advantage">
  <div class="pattern-zone" style="left:0;top:300px;width:360px;height:200px" role="img" aria-label="Faint geometric background pattern"></div>
  <div class="pattern-zone" style="left:680px;top:0;width:134px;height:90px" role="img" aria-label="Faint geometric background pattern"></div>

  <h2 class="section-title" style="left:46px;top:52px"><span class="light">COMPETITIVE</span><span class="bold">ADVANTAGE</span></h2>
  <div class="dot-rule" style="left:48px;top:120px"></div>
  <div class="body-copy" style="left:50px;top:135px;width:270px">
    <p>Our competitive advantage lies in the uniqueness of our property investment opportunities. Unlike traditional real estate companies, we focus on offering properties that are not only profitable but also aesthetically pleasing and unique. By catering to the tastes of architecture lovers, we set ourselves apart from the competition and attract a niche market of customers who appreciate the artistry and design of our projects.</p>
    <p class="note">Additionally, the streamlined and condensed timelines facilitated by our modular approach provide quicker returns on investment.</p>
  </div>

  <div class="frame" style="left:40px;top:250px;width:140px;height:145px"></div>
  <div class="photo" style="left:50px;top:266px;width:146px;height:144px;background:linear-gradient(180deg,#eef0f0 0%,#d8dada 25%,#2d2d2d 42%,#555 60%,#6d8a3a 80%,#4f6a28 100%)" role="img" aria-label="Dark cantilevered modular home over a grassy slope"></div>
  <div class="frame" style="left:140px;top:345px;width:180px;height:110px"></div>
  <div class="photo" style="left:160px;top:360px;width:144px;height:143px;background:linear-gradient(180deg,#cfcfcf 0%,#e9e9e8 40%,#9d9a97 70%,#5d5b59 100%)" role="img" aria-label="Minimal bedroom interior with a large window view"></div>

  <div class="frame" style="left:425px;top:200px;width:160px;height:160px"></div>
  <div class="photo" style="left:436px;top:38px;width:142px;height:212px;background:linear-gradient(180deg,#f0f1f1 0%,#d7d9d9 35%,#3b3a38 55%,#6c7a4a 78%,#4c5a30 100%)" role="img" aria-label="Modern dark home with lit garden path at dusk"></div>
  <div class="photo" style="left:436px;top:262px;width:142px;height:218px;background:linear-gradient(180deg,#b9cad6 0%,#9fb0b9 30%,#6b6650 55%,#4a4636 80%,#3a3729 100%)" role="img" aria-label="Remote hillside home among rolling ranges"></div>

  <h2 class="section-title" style="left:613px;top:52px"><span class="light">FINANCIAL</span><span class="bold">SUMMARY</span></h2>
  <div class="dot-rule" style="left:615px;top:120px"></div>
  <div class="body-copy" style="left:615px;top:138px;width:172px">
    <p>In terms of financial projections, with each development, we anticipate a profit of 10%-20% which will be project dependent.</p>
    <p>This growth is fueled by the increasing demand for unique property investments in New Zealand and our ability to deliver high-quality services to the market in a condensed time frame, with heavily controlled costs.</p>
    <p>With a solid business model and a dedicated team, we are confident in our ability to achieve success and establish Tarrow Dwellings Investments as a trusted name in the industry.</p>
    <p>New Zealand's property market has been experiencing steady growth over the years, making it an attractive destination for property investments. With its beautiful landscapes and strong economy, New Zealand offers a diverse range of investment opportunities for both local and international investors. The demand for quality properties in prime locations continues to rise, creating a favorable environment for property investment companies like ours that can lean on our modular benefits of being able to reach unique and remote locations.</p>
  </div>

  <div class="page-footer" style="left:45px">www.tarrowdwellings.co.nz<span class="rule"></span><span class="num">3</span></div>
  <div class="page-footer" style="left:450px">www.tarrowdwellings.co.nz<span class="rule"></span><span class="num">4</span></div>
</section>

</body>
</html>
```